Banner & also another minor digital image for an Online Academic Journal

A direct example of what I need can be found in this webpage: http://scholarvault.wbn-edu.example/qtrv/
(Please see attached files, "sAMPLE", and "sAMPLE 2", so you can see what I mean.)
This link (http://scholarvault.wbn-edu.example/qtrv/) is for an existing ONLINE ACADEMIC JOURNAL at the Halvercrest University.
It will help for you to be acquainted with the format of Online Academic Journals.
You will find that there is a banner on top as well as a digital image of a journal/book cover on the right.
I need a
(1) banner and
a (2) digital journal/book cover
for a website for an ONLINE ACADEMIC JOURNAL.
I am looking for a serious, professional, elegant design.
There will not be a print version. Only web-based online publication. No coding needed, only PSD, JPG/PNG and PDF.
1) We use Quillora (http://archivenest.quillora.example/repository-software/journals/) for the digital image of the journal/book cover layout. Link shows the general layout of the journal website.
2) For the digital image of the journal/book cover and also the banner,
Name of the journal is....
"Solace: A Journal on Coercive Harm and Trafficking"
Only this text will be used and applied to both banner and cover.
***The color associated with the theme of dignity is purple
****You could also add the color red.
*****I don't want the design to be garish, but accents in red might represent
the sexual exploitation and violence in the title.
3) Attached "sAmple 2" file is a basic design for the digital image of the journal/book cover from Quillora. I am looking for something more elegant and professional looking. Your creativity is encouraged. I am open to receiving your interpretation.
Academics & Community Professionals
Non Profit
Match journal design

```html
<!DOCTYPE html>
<html lang="en">
<head>
<meta charset="utf-8">
<title>Solace: A Journal on Coercive Harm and Trafficking — Banner</title>
<link href="https://fonts.googleapis.com/css2?family=Michroma&display=swap" rel="stylesheet">
<style>
  :root {
    --plum: #6d4380;
    --plum-light: #7f5395;
    --lavender-strip: #ddd6e2;
    --crimson-panel: #ad2f55;
    --rose: #b8325f;
    --white: #ffffff;
  }
  html, body {
    margin: 0;
    padding: 0;
    width: 1200px;
    height: 191px;
    overflow: hidden;
    background: var(--plum);
  }
  .banner {
    position: relative;
    width: 1200px;
    height: 191px;
    overflow: hidden;
    background: var(--plum);
  }
  .banner__mosaic-area {
    position: absolute;
    left: 545px;
    top: 0;
    width: 655px;
    height: 183px;
    background:
      radial-gradient(ellipse 260px 120px at 45% 40%, rgba(200, 40, 80, 0.55), transparent 70%),
      radial-gradient(ellipse 200px 110px at 85% 60%, rgba(170, 50, 95, 0.4), transparent 70%),
      linear-gradient(90deg, var(--plum) 0%, var(--plum-light) 55%, var(--plum) 100%);
  }
  .banner__strip {
    position: absolute;
    left: 0;
    bottom: 0;
    width: 1200px;
    height: 8px;
    background: var(--lavender-strip);
  }
  .banner__title-panel {
    position: absolute;
    left: 0;
    top: 27px;
    width: 545px;
    height: 132px;
    background: var(--crimson-panel);
  }
  .banner__title {
    position: absolute;
    left: 70px;
    top: 38px;
    margin: 0;
    font-family: "Michroma", "Arial", sans-serif;
    font-weight: 400;
    font-variant: small-caps;
    font-size: 27px;
    line-height: 40px;
    letter-spacing: 1.5px;
    color: var(--white);
    -webkit-text-stroke: 0.4px var(--white);
  }
  .banner__title span { display: block; white-space: nowrap; }
</style>
</head>
<body>
  <header class="banner">
    <div class="banner__mosaic-area" role="img" aria-label="Mosaic of overlapping purple and crimson squares"></div>
    <div class="banner__strip"></div>
    <div class="banner__title-panel"></div>
    <h1 class="banner__title">
      <span>A Journal on</span>
      <span>Coercive Harm</span>
      <span>and Trafficking</span>
    </h1>
  </header>
</body>
</html>
```